Home page design for a New Zealand clothing business

- The design must be based around the attached HPID (home page information design) called Copper Ridge HPID. I've attached Word and PDF versions - these are the same. The table boxes are just for approximate placement of information – you DON'T have to make it look exactly like this. All fonts used in the HPID are only examples - you can use any Google font you wish.

- Information only is in orange text. Copy to go on the design in black text. Some instructions are in the HPID. Please be creative!

- The design needs to be modern. Colours are to be mainly black and white (like the logo) and the accent colour is to be brown.

- I've provided the images for the galleries - they are labelled and will match the name in the HPID.

- One possibility is to have a large background image for the whole design. I've added one example image for this: NZ landscape background image.jpg You could supply one of your designs on a white background, and one on this landscape background.

- These are some websites that are similar with the products they sell. Please DON'T copy these sites but they are good examples....
http://www.tolmerapparel.co.nz/
http://www.quillet.co.nz/
http://www.vornak.co.nz/
http://www.pelhurst.co.nz/

Width of content will be 1100 pixels when implemented as a web page. Header height (without nav bar) 150-160 pixels.

The winning PSD file will have to be provided as follows…
1. Canvas size of 2000px x 2000px - 72ppi in Adobe Photoshop (CS5 compatible)
2. Width of content section is 1100px wide - centered in the canvas
3. Any button rollovers/hovers in the PSD as hidden layers.
4. All fonts used must be Google fonts (except for the fonts in the header at the top of the page).
5. You will need to supply the chosen home page plus one example page (example page as a style guide for how all other pages will look). Example page is only the header and navigational bar at the top, an empty sector in the middle with a column (180 px wide) which can be left or right aligned which means the main sector is 920 pixels wide, and then the footer at the bottom of the page

```html
<!DOCTYPE html>
<html lang="en">
<head>
<meta charset="utf-8">
<title>Copper Ridge — Traditional oilskin &amp; woollen clothing</title>
<link href="https://fonts.googleapis.com/css2?family=Titillium+Web:wght@400;600&display=swap" rel="stylesheet">
<style>
:root{
  --ink:#231f20;
  --white:#ffffff;
  --grey-nav:#c9c9c9;
  --grey-label:#c4c4c4;
  --grey-foot:#e4e4e4;
  --red:#b5121b;
  --dark-btn:#333333;
  --orange:#ee7421;
  --text:#333333;
  --muted:#555555;
}
*{box-sizing:border-box;margin:0;padding:0}
html,body{width:754px;height:1200px;overflow:hidden}
body{position:relative;background:var(--white);font-family:"Titillium Web",sans-serif;color:var(--text)}
.abs{position:absolute}

.site-header{left:0;top:0;width:754px;height:70px;background:var(--ink);color:var(--white)}
.brand{left:64px;top:20px;display:flex;align-items:center;gap:6px;font-size:17px;font-weight:600;color:var(--white);white-space:nowrap}
.brand-dot{width:14px;height:14px;border-radius:50%;border:2px solid var(--white)}
.tagline{left:288px;top:8px;font-size:9.5px;line-height:12px}
.tagline small{display:block;font-size:7.5px}
.cart{left:289px;top:36px;width:86px;height:19px;background:var(--white);color:var(--muted);font-size:7px;line-height:19px;padding-left:8px;border-radius:2px}
.search{left:384px;top:36px;width:86px;height:19px;background:var(--white);color:var(--muted);font-size:7px;line-height:19px;padding-left:5px;border-radius:2px}
.search svg{position:absolute;right:5px;top:5px}
.header-info{right:63px;top:17px;text-align:right;font-size:7.5px;line-height:11px}

.main-nav{left:0;top:70px;width:754px;height:36px;background:var(--grey-nav);display:flex;justify-content:center}
.main-nav a{color:var(--text);text-decoration:none;font-size:7.5px;line-height:36px;padding:0 14px}

.hero{left:0;top:106px;width:754px;height:323px;background:linear-gradient(180deg,#a9b4bd 0%,#8a8f6e 22%,#6d6a5e 45%,#8d8780 70%,#a7a39c 100%)}
.hero-panel{left:63px;top:177px;width:151px;height:174px;background:rgba(40,36,34,.72);color:var(--white);padding:14px 12px}
.hero-panel h1{font-size:21px;font-weight:600;line-height:24px;margin-bottom:4px}
.hero-panel p{font-size:10.5px;line-height:22px;font-weight:600}
.hero-cta{left:77px;top:296px;width:130px;height:29px;background:var(--red);color:var(--white);font-size:10px;font-weight:600;line-height:29px;text-align:center}
.arrow{width:19px;height:19px;border-radius:50%;background:var(--white);top:244px}
.arrow svg{display:block;margin:5px}
.dots{left:356px;top:401px;display:flex;gap:5px}
.dots i{width:8px;height:8px;border-radius:50%;background:var(--white);display:block}
.dots i.on{background:var(--red)}

.welcome{left:70px;top:440px;width:614px;text-align:center}
.welcome h2{font-size:14px;font-weight:400;color:var(--ink);margin-bottom:8px}
.welcome p{font-size:7.3px;line-height:15px;color:var(--muted)}

.card{top:568px;width:147px}
.card-photo{height:106px}
.card-label{height:27px;background:var(--grey-label);font-size:8.8px;line-height:27px;padding-left:6px;color:var(--text)}
.card-text{font-size:6.8px;line-height:11.3px;margin-top:8px;height:46px;color:var(--text)}
.card-btns{display:flex;justify-content:space-between;margin-top:5px}
.btn{width:70px;height:25px;font-size:7px;line-height:25px;text-align:center;color:var(--white);border-radius:2px}
.btn-view{background:var(--red)}
.btn-buy{background:var(--dark-btn)}

.promo{left:63px;top:822px;width:628px;height:94px;background:linear-gradient(180deg,#4a4a49,#5b5c4f 60%,#3b3a36);color:var(--white)}
.promo p{position:absolute;left:40px;top:30px;width:530px;text-align:center;font-size:10.8px;line-height:19px}
.promo-map{position:absolute;right:0;top:0;width:54px;height:94px;background:#050505}
.promo-map span{position:absolute;left:10px;top:14px;width:34px;height:66px;background:linear-gradient(160deg,#e8e8e8,#bdbdbd);border-radius:40% 20% 40% 20%}

.site-footer{left:0;top:939px;width:754px;height:201px;background:var(--grey-foot)}
.foot-links{left:63px;top:14px;font-size:7px;line-height:15.2px;list-style:none}
.foot-brand{left:63px;top:158px;display:flex;align-items:center;gap:5px;font-size:12px;font-weight:600;color:var(--ink)}
.foot-brand i{width:10px;height:10px;border-radius:50%;border:1.5px solid var(--ink);display:block}
.foot-cats{left:189px;top:14px;font-size:7px;line-height:15.2px;list-style:none}
.foot-cats .cat{font-size:10.5px;color:var(--red);line-height:17px}
.signup{left:288px;top:11px;width:216px}
.signup h3{font-size:8.8px;line-height:15px;font-weight:600;color:var(--red)}
.field{width:208px;height:32px;background:var(--white);border:1px solid #cfcfcf;font-size:7px;line-height:30px;padding-left:8px;margin-top:8px}
.signup .refer{font-size:7px;margin-top:9px}
.refer-btn{width:84px;height:31px;background:var(--red);color:var(--white);font-size:7.5px;line-height:31px;text-align:center;margin-top:7px}
.partner{left:566px;top:11px;width:125px}
.partner-mark{height:24px;background:var(--ink);color:var(--white);font-size:9px;font-weight:600;line-height:24px;text-align:center}
.partner p{font-size:7px;line-height:15.2px;text-align:center;margin-top:16px}
.partner-btn{height:34px;background:var(--orange);color:var(--white);font-size:7.5px;line-height:34px;text-align:center;margin-top:11px;border-bottom:2px solid #b9561a}

.site-bottom{left:0;top:1140px;width:754px;height:60px;background:var(--ink);color:var(--white)}
.copyright{left:63px;top:24px;font-size:7px}
.social{right:63px;top:22px;display:flex;gap:6px}
.social i{width:15px;height:15px;border-radius:2px;display:block}
</style>
</head>
<body>

<header class="site-header abs">
  <div class="brand abs"><span class="brand-dot"></span>Copper Ridge</div>
  <div class="tagline abs">Traditional oilskin &amp; woollen clothing<small>Stores in Ashcombe &amp; Wrenford | Online Shop</small></div>
  <div class="cart abs">Cart 0 items &nbsp; 8.00$</div>
  <div class="search abs">Search
    <svg width="9" height="9" viewBox="0 0 10 10"><circle cx="4" cy="4" r="3" fill="none" stroke="#222" stroke-width="1.4"/><line x1="6.3" y1="6.3" x2="9" y2="9" stroke="#222" stroke-width="1.4"/></svg>
  </div>
  <div class="header-info abs">Free delivery over $99 NZ wide<br>Worldwide sales welcome<br>0800 555 019</div>
</header>

<nav class="main-nav abs">
  <a>Home</a><a>About Us</a><a>Oilskin</a><a>Wool</a><a>Trousers</a><a>Gift Vouchers</a><a>Embroidery/Branding</a><a>Customer Service</a><a>Contact/Map</a>
</nav>

<section class="hero abs" role="img" aria-label="Two young children in oilskin vests standing on a gravel farm yard with wooden fences and green hills"></section>
<div class="hero-panel abs">
  <h1>Copper Ridge</h1>
  <p>Warm<br>Smart<br>Comfortable</p>
</div>
<div class="hero-cta abs">Made in New Zealand</div>
<div class="arrow abs" style="left:26px"><svg width="9" height="9" viewBox="0 0 10 10"><path d="M7 1 L3 5 L7 9" fill="none" stroke="#333" stroke-width="2"/></svg></div>
<div class="arrow abs" style="left:712px"><svg width="9" height="9" viewBox="0 0 10 10"><path d="M3 1 L7 5 L3 9" fill="none" stroke="#333" stroke-width="2"/></svg></div>
<div class="dots abs"><i class="on"></i><i></i><i></i></div>

<section class="welcome abs">
  <h2>Welcome To Copper Ridge</h2>
  <p>Lorem ipsum dolor sit amet, consectetuer adipiscing elit, sed diam nonummy nibh euismod tincidunt ut laoreet dolore magna aliquam erat volutpat. Ut wisi enim ad minim veniam, quis nostrud exerci tation ullamcorper suscipit lobortis nisl ut aliquip ex ea commodo consequat. Lorem ipsum dolor sit amet, consectetuer adipiscing elit, sed diam nonummy nibh euismod tincidunt ut laoreet dolore magna aliquam erat volutpat. Ut wisi enim ad minim veniam, quis nostrud exerci tation ullamcorper suscipit lobortis nisl ut aliquip ex ea commodo consequat.</p>
</section>

<article class="card abs" style="left:63px">
  <div class="card-photo" role="img" aria-label="Man in hi-vis oilskin vest sitting by farm silos on the phone" style="background:linear-gradient(180deg,#9aa3a6,#6e6c5c 60%,#4b4a44)"></div>
  <div class="card-label">Oilskins</div>
  <p class="card-text">Premium oilskin vests and jackets in a range of smart and practical designs. Ask us about our monogramming service.</p>
  <div class="card-btns"><span class="btn btn-view">View</span><span class="btn btn-buy">Buy</span></div>
</article>
<article class="card abs" style="left:224px">
  <div class="card-photo" role="img" aria-label="Man in dark oilskin vest and hat leaning on a rail in a woolshed" style="background:linear-gradient(180deg,#4c4038,#6a5a49 55%,#3a332c)"></div>
  <div class="card-label">Hi-vis oilskins</div>
  <p class="card-text">Short sleeve and sleeveless hi vis oilskin vests – protection from the elements while being seen. Ask us about our monogram-ming service.</p>
  <div class="card-btns"><span class="btn btn-view">View</span><span class="btn btn-buy">Buy</span></div>
</article>
<article class="card abs" style="left:384px">
  <div class="card-photo" role="img" aria-label="Woollen socks resting on a weathered fence post" style="background:linear-gradient(180deg,#9b8d86,#7c6b64 55%,#5e4b43)"></div>
  <div class="card-label">Kids' oilskins</div>
  <p class="card-text">Be just like the grown-ups! Sizes 2 to 14 kids' oilskin sleeveless vests. Keep warm outside! Ask us about our monogramming service.</p>
  <div class="card-btns"><span class="btn btn-view">View</span><span class="btn btn-buy">Buy</span></div>
</article>
<article class="card abs" style="left:545px">
  <div class="card-photo" role="img" aria-label="Young man in a woollen jacket and wide-brim hat by a paddock fence" style="background:linear-gradient(180deg,#9fb09a,#6f7a60 55%,#4d4b44)"></div>
  <div class="card-label">Woollen clothing</div>
  <p class="card-text">Get kitted out with all your winter woollen clothing – gloves, hats, singlets, tees and jerseys. Ask us about our monogramming service.</p>
  <div class="card-btns"><span class="btn btn-view">View</span><span class="btn btn-buy">Buy</span></div>
</article>

<section class="promo abs" role="img" aria-label="Dark Southland hill landscape behind the brand message">
  <p>Copper Ridge is a Southland family-owned business. All oilskin and woollen clothing is 100% New Zealand made. More keyworded text in this area about the brand and the business...</p>
  <div class="promo-map" role="img" aria-label="Map of New Zealand"><span></span></div>
</section>

<footer class="site-footer abs">
  <ul class="foot-links abs"><li>Home</li><li>About Us</li><li>Testimonials</li><li>Gift Vouchers</li><li>Embroidery/Branding</li><li>Customer Service</li><li>Contact/Map</li></ul>
  <div class="foot-brand abs"><i></i>Copper Ridge</div>
  <ul class="foot-cats abs"><li class="cat">Oilskin</li><li>Vest</li><li>Jackets</li><li>Hi-viz</li><li class="cat">Wool</li><li>Jerseys</li><li>Singlets</li><li>Socks</li><li>Gloves</li><li>Hats</li></ul>
  <div class="signup abs">
    <h3>Sign up to get our regular but occasional email letting you know what the latest news and deals are with Copper Ridge...</h3>
    <div class="field" style="margin-top:10px">File Name</div>
    <div class="field">Email address</div>
    <p class="refer">Refer the Copper Ridge website to a friend:</p>
    <div class="refer-btn">Click Here</div>
  </div>
  <div class="partner abs">
    <div class="partner-mark">Tasman Workgear</div>
    <p>Info on Tasman Workgear will go here for the next 4-5 lines so please use lorum ipsum text for 4-5 lines....</p>
    <div class="partner-btn">Visit Tasman Workgear website</div>
  </div>
</footer>

<div class="site-bottom abs">
  <p class="copyright abs">© 2014 Company Name &nbsp;All right reserved &nbsp;Term of Use</p>
  <div class="social abs"><i style="background:#3b5998"></i><i style="background:#55acee"></i><i style="background:#0e76a8"></i><i style="background:#f26522"></i></div>
</div>

</body>
</html>
```